Web Design For Staffing Company

We need a homepage web design for a technical staffing company.

Please see attached brief for project details.

please make the site modern with bold colors while matching the logo

Be sure to read the attached breif in full beforehand.

Target Market(s)

technical companies looking to hire talent

Industry/Entity Type

Staffing

Number of Pages Required

1 page

Font styles to use
Sans Serif

```html
<!DOCTYPE html>
<html lang="en">
<head>
<meta charset="utf-8">
<title>Veltrix Staffing — Home</title>
<link rel="stylesheet" href="https://fonts.googleapis.com/css2?family=Montserrat:wght@400;500;600;700;800&display=swap">
<style>
:root{
  --stage:#1b3e60;
  --navy:#173a5c;
  --navy-deep:#163655;
  --blue:#2b7bc4;
  --blue-bright:#2f80c9;
  --ink:#1d2a36;
  --muted:#8a939c;
  --line:#e4e8ec;
  --ring:#dbe9f5;
  --white:#ffffff;
}
*{box-sizing:border-box;margin:0;padding:0}
html,body{width:1200px;height:4494px;overflow:hidden}
body{background:var(--stage);font-family:'Montserrat',sans-serif;color:var(--ink)}
.page{position:absolute;left:0;top:165px;width:1200px;height:4164px;background:var(--white);overflow:hidden}

/* header */
.site-header{height:90px;display:flex;align-items:center;justify-content:space-between;padding:0 112px 0 108px;background:var(--white)}
.brand{display:flex;align-items:center;gap:12px;font-weight:800;font-size:36px;color:var(--navy);letter-spacing:.5px}
.brand-mark{width:20px;height:20px;background:var(--blue);border-radius:50%}
.brand small{font-size:0}
.nav{display:flex;gap:32px;font-size:13px;font-weight:500;color:var(--ink)}
.nav a{color:inherit;text-decoration:none}
.nav a.active{color:var(--blue)}

/* hero */
.hero{position:relative;height:710px}
.hero-photo{position:absolute;inset:0;background:linear-gradient(120deg,#d9dcdf 0%,#b7b3ad 35%,#8e8a86 60%,#5d6064 85%,#3d4248 100%)}
.hero-shade{position:absolute;inset:0;background:rgba(20,40,60,.18)}
.hero-content{position:relative;text-align:center;padding-top:234px}
.hero h1{color:var(--white);font-size:38px;font-weight:700;line-height:52px}
.search{display:flex;width:674px;height:54px;margin:46px auto 0;background:var(--white)}
.search .field{flex:1;display:flex;align-items:center;gap:8px;padding:0 26px;font-size:12px;color:#a7adb3;border-right:1px solid var(--line)}
.search .field:nth-child(2){border-right:0}
.search button{width:178px;border:0;background:var(--blue);color:var(--white);font:600 12px 'Montserrat',sans-serif;display:flex;align-items:center;justify-content:center;gap:8px}

/* about */
.about{height:357px;background:var(--navy);color:var(--white);text-align:center;padding-top:70px}
.about h2{font-size:26px;font-weight:700;margin-bottom:22px}
.about p{width:720px;margin:0 auto;font-size:21px;line-height:37px}

/* features */
.features{position:relative;height:925px}
.ring{position:absolute;border:16px solid var(--ring);border-radius:50%}
.features .ring{width:220px;height:220px;right:-140px;top:72px}
.feature{position:absolute}
.photo-blob{position:absolute;border-radius:48% 52% 44% 56% / 52% 40% 60% 48%}
.blob-accent{position:absolute;border-radius:50% 46% 52% 48% / 50% 54% 46% 50%;background:var(--blue)}
.feature h3{font-size:32px;font-weight:700;line-height:44px;color:var(--ink)}
.feature p{font-size:12px;line-height:24px;color:var(--muted);margin-top:22px;width:370px}
.btns{display:flex;gap:16px;margin-top:30px}
.btn{width:150px;height:42px;display:flex;align-items:center;justify-content:center;font-size:12px;font-weight:600;letter-spacing:.3px}
.btn.solid{background:var(--blue);color:var(--white)}
.btn.outline{border:2px solid var(--ink);color:var(--ink)}

/* testimonial */
.testimonial{position:relative;height:466px;color:var(--white);text-align:center}
.testimonial .bg{position:absolute;inset:0;background:linear-gradient(90deg,#2a72b8,#3283cb 50%,#2a72b8)}
.testimonial .inner{position:relative;padding-top:56px}
.testimonial h2{font-size:28px;font-weight:700}
.testimonial blockquote{width:600px;margin:30px auto 0;font-size:17px;line-height:30px}
.avatar{width:50px;height:50px;border-radius:50%;background:#d5dde5;border:2px solid var(--white);margin:26px auto 0}
.testimonial cite{display:block;margin-top:20px;font-style:normal;font-size:13px}
.arrow{position:absolute;top:190px;width:44px;height:44px;border-radius:50%;border:1px solid rgba(255,255,255,.6);display:flex;align-items:center;justify-content:center}

/* blog */
.blog{position:relative;height:742px;text-align:center}
.blog .ring{width:200px;height:200px;left:-120px;top:40px}
.blog h2{padding-top:84px;font-size:38px;font-weight:700;color:var(--navy)}
.blog .lead{width:700px;margin:16px auto 0;font-size:13px;line-height:30px;color:var(--muted)}
.posts{display:flex;gap:16px;position:absolute;left:106px;top:246px}
.post{width:318px;height:438px;background:var(--white);box-shadow:0 6px 20px rgba(20,40,60,.08);text-align:left}
.post-img{height:195px}
.post-body{display:flex;gap:20px;padding:26px 20px 0 24px}
.date{text-align:center;color:var(--navy)}
.date b{display:block;font-size:26px;font-weight:600;color:var(--blue)}
.date span{font-size:11px;font-weight:600}
.post h4{font-size:16px;font-weight:600;margin-top:6px;white-space:nowrap}
.post p{font-size:11.5px;line-height:24px;color:var(--muted);margin-top:16px;width:200px}
.post .meta{font-size:10px;color:#b2b9c0;margin-top:26px}

/* cta */
.cta{height:484px;display:flex;gap:18px;padding:48px 24px 0}
.cta-card{position:relative;width:566px;height:420px;overflow:hidden}
.cta-card .photo{position:absolute;inset:0}
.cta-card .body{position:relative;padding:152px 0 0 84px;color:var(--white)}
.cta-card h3{font-size:28px;font-weight:800;line-height:36px;text-transform:uppercase}
.cta-btn{margin-top:20px;display:inline-flex;align-items:center;gap:10px;height:38px;padding:0 22px;background:var(--white);color:var(--navy);font-size:12px;font-weight:600}

/* footer */
.site-footer{height:305px;background:var(--navy-deep);color:var(--white);position:relative}
.site-footer .brand{position:absolute;left:108px;top:66px;color:var(--white)}
.fcol{position:absolute;top:62px;width:200px}
.fcol h5{font-size:14px;font-weight:600}
.fcol p{font-size:12px;line-height:24px;color:#a9b8c7;margin-top:20px}
.fbtn{position:absolute;top:210px;width:150px;height:36px;background:var(--blue);display:flex;align-items:center;justify-content:center;gap:8px;font-size:12px;font-weight:600;color:var(--white)}
.copy{height:84px;background:var(--navy);display:flex;align-items:center;justify-content:center;font-size:12px;color:#9fb0c0;border-top:1px solid rgba(255,255,255,.06)}
</style>
</head>
<body>
<div class="page">

  <header class="site-header">
    <div class="brand"><span class="brand-mark"></span>Veltrix</div>
    <nav class="nav">
      <a class="active" href="#">HOME</a><a href="#">ABOUT</a><a href="#">JOB SEEKERS</a><a href="#">CLIENTS</a><a href="#">BLOG</a><a href="#">CONTACT</a>
    </nav>
  </header>

  <section class="hero">
    <div class="hero-photo" role="img" aria-label="Photo of smiling professionals talking in a bright office"></div>
    <div class="hero-shade"></div>
    <div class="hero-content">
      <h1>The Right People For<br>The Right Jobs!</h1>
      <div class="search">
        <div class="field">Keyword</div>
        <div class="field">
          <svg width="12" height="14" viewBox="0 0 12 14"><path d="M6 1a4 4 0 0 1 4 4c0 3-4 8-4 8S2 8 2 5a4 4 0 0 1 4-4z" fill="none" stroke="#a7adb3" stroke-width="1.2"/><circle cx="6" cy="5" r="1.4" fill="#a7adb3"/></svg>
          Location
        </div>
        <button><svg width="13" height="13" viewBox="0 0 13 13"><circle cx="5.5" cy="5.5" r="4" fill="none" stroke="#fff" stroke-width="1.6"/><path d="M8.5 8.5l3.5 3.5" stroke="#fff" stroke-width="1.6"/></svg>Search Jobs</button>
      </div>
    </div>
  </section>

  <section class="about">
    <h2>About Us</h2>
    <p>Veltrix Staffing is a National Technical Staffing and Recruiting Solutions Provider founded in 2013 focused on matching contract and full time Engineering and IT professionals with new and exciting employment opportunities!</p>
  </section>

  <section class="features">
    <div class="ring"></div>

    <div class="feature" style="left:106px;top:98px;width:378px;height:326px">
      <div class="blob-accent" style="left:200px;top:20px;width:178px;height:290px"></div>
      <div class="photo-blob" style="left:0;top:0;width:362px;height:326px;background:linear-gradient(135deg,#eef1f4,#c9cfd6 55%,#9aa6b2)" role="img" aria-label="Photo of a presenter speaking to seated colleagues"></div>
    </div>
    <div class="feature" style="left:638px;top:150px">
      <h3>We love to recruit!</h3>
      <p>Simply said... WE LOVE TO RECRUIT! It's our passion and we take it very seriously! It is not easy for JOB SEEKERS to put their job search efforts and trust in the hands of</p>
      <div class="btns"><span class="btn solid">LEARN MORE</span><span class="btn outline">VIEW JOBS</span></div>
    </div>

    <div class="feature" style="left:190px;top:530px">
      <h3>Are you responsible<br>for Technical Staffing?</h3>
      <p>Within your organization? Are you satisfied with your current Supplier(s)' overall performance? Does it appear they identify potential Candidate(s) based purely on</p>
      <div class="btns"><span class="btn solid">LEARN MORE</span><span class="btn outline">HIRE TALENT</span></div>
    </div>
    <div class="feature" style="left:700px;top:496px;width:392px;height:326px">
      <div class="blob-accent" style="left:0;top:60px;width:170px;height:250px"></div>
      <div class="photo-blob" style="left:12px;top:0;width:376px;height:326px;background:linear-gradient(135deg,#f3f4f5,#d8dade 50%,#a8b3bf)" role="img" aria-label="Photo of a man drawing a chart on a whiteboard"></div>
    </div>
  </section>

  <section class="testimonial">
    <div class="bg" role="img" aria-label="Blue-tinted photo of a team meeting"></div>
    <div class="inner">
      <h2>Testimonial</h2>
      <blockquote>"Mark Dalen is an excellent recruiter. He is articulate, honest, has a good nature and is an effective information conduit between his clients and candidates. He gave me the feeling he is there for the big picture desiring to forge a future relationship that will be mutually beneficial to both of us."</blockquote>
      <div class="avatar" role="img" aria-label="Portrait of the reviewer"></div>
      <cite>Sam R. - Electrical Test Engineer in the Automotive Sector</cite>
    </div>
    <span class="arrow" style="left:192px"><svg width="10" height="14" viewBox="0 0 10 14"><path d="M7 2L2 7l5 5" fill="none" stroke="#fff" stroke-width="1.6"/></svg></span>
    <span class="arrow" style="right:188px"><svg width="10" height="14" viewBox="0 0 10 14"><path d="M3 2l5 5-5 5" fill="none" stroke="#fff" stroke-width="1.6"/></svg></span>
  </section>

  <section class="blog">
    <div class="ring"></div>
    <h2>Veltrix Blog</h2>
    <p class="lead">Lorem ipsum dolor sit amet, consectetur adipisicing elit, sed do eiusmod tempor incididunt ut labore et dolore magna aliqua. Ut enim ad minim veniam, quis nostrud exercitation</p>
    <div class="posts">
      <article class="post">
        <div class="post-img" style="background:linear-gradient(135deg,#2d3e56,#6a7f98 60%,#c7d0d9)" role="img" aria-label="Photo of a woman working on a laptop"></div>
        <div class="post-body">
          <div class="date"><b>28</b><span>JUN</span></div>
          <div><h4>Ways To Make The...</h4><p>"This is the tightest labor market I can remember. Unemployment is at a 50-year low and wage growth is at 3.2%," said Jed</p><div class="meta">1 COMMENT</div></div>
        </div>
      </article>
      <article class="post">
        <div class="post-img" style="background:linear-gradient(135deg,#4a8fd0,#9cc4e8 55%,#d9e6f1)" role="img" aria-label="Photo of a business handshake"></div>
        <div class="post-body">
          <div class="date"><b>28</b><span>JUN</span></div>
          <div><h4>Meeting Employees'...</h4><p>The benefits of employee satisfaction are well-established, so HR professionals and leaders across all industries spend a</p><div class="meta">1 COMMENT</div></div>
        </div>
      </article>
      <article class="post">
        <div class="post-img" style="background:linear-gradient(135deg,#5f6b77,#aeb7c0 55%,#e2e6ea)" role="img" aria-label="Image of a robotic brain"></div>
        <div class="post-body">
          <div class="date"><b>28</b><span>JUN</span></div>
          <div><h4>Will Robots Take...</h4><p>Have you been to this website? While we might be skeptical of any analysis that generalizes threats and opportunities in the</p><div class="meta">1 COMMENT</div></div>
        </div>
      </article>
    </div>
  </section>

  <section class="cta">
    <div class="cta-card">
      <div class="photo" style="background:linear-gradient(120deg,#1f3550,#4c6583 55%,#8e9aa8)" role="img" aria-label="Photo of a smiling team of professionals"></div>
      <div class="body">
        <h3>Looking for<br>career-minded<br>candidates?</h3>
        <span class="cta-btn"><svg width="13" height="13" viewBox="0 0 13 13"><path d="M2 11h9M3 8l6-6 2 2-6 6H3z" fill="none" stroke="#173a5c" stroke-width="1.3"/></svg>Request Talent</span>
      </div>
    </div>
    <div class="cta-card">
      <div class="photo" style="background:linear-gradient(120deg,#3a4a5c,#6b7888 55%,#a89385)" role="img" aria-label="Photo of a young professional woman in glasses"></div>
      <div class="body">
        <h3>Looking<br>for career<br>opportunities?</h3>
        <span class="cta-btn"><svg width="13" height="13" viewBox="0 0 13 13"><circle cx="5.5" cy="5.5" r="4" fill="none" stroke="#173a5c" stroke-width="1.5"/><path d="M8.5 8.5l3.5 3.5" stroke="#173a5c" stroke-width="1.5"/></svg>Search jobs</span>
      </div>
    </div>
  </section>

  <footer class="site-footer">
    <div class="brand"><span class="brand-mark"></span>Veltrix</div>
    <div class="fcol" style="left:356px"><h5>Get Hired</h5><p>Search our extensive list of available jobs to find your ideal match.</p></div>
    <div class="fcol" style="left:601px"><h5>Hire Talent</h5><p>We' re here to provide the people you need to get work done.</p></div>
    <div class="fcol" style="left:846px"><h5>Get in Touch</h5><p>Veltrix Staffing, Inc.<br>220 Harbor Lane, Bldg. 2,<br>3rd floor Easton,<br>MA 02100</p></div>
    <span class="fbtn" style="left:356px"><svg width="12" height="12" viewBox="0 0 13 13"><circle cx="5.5" cy="5.5" r="4" fill="none" stroke="#fff" stroke-width="1.5"/><path d="M8.5 8.5l3.5 3.5" stroke="#fff" stroke-width="1.5"/></svg>Search Now</span>
    <span class="fbtn" style="left:601px"><svg width="12" height="12" viewBox="0 0 12 12"><circle cx="6" cy="4" r="2.6" fill="none" stroke="#fff" stroke-width="1.3"/><path d="M1.5 11.5a4.5 4.5 0 0 1 9 0" fill="none" stroke="#fff" stroke-width="1.3"/></svg>Start Today</span>
    <span class="fbtn" style="left:846px"><svg width="14" height="11" viewBox="0 0 14 11"><rect x="1" y="1" width="12" height="9" fill="none" stroke="#fff" stroke-width="1.2"/><path d="M1 1l6 5 6-5" fill="none" stroke="#fff" stroke-width="1.2"/></svg>Contact Us</span>
  </footer>
  <div class="copy">© 2020 Veltrix Staffing, Inc. All rights reserved.</div>

</div>
</body>
</html>
```